Professional and creatice Life Coach - Business Card design

I just relaunched my website and now i a need a correspoonding business card for my task as life coach. My website is www.dlorvan.net as reference. The compass is kind of a symbol for my work, as I help people navigate through their challenging phases in life. The business card should be colorful, but not too playful as I also adress business people. So it sould be creative, but professional (also to suport my other business as Management Consultant)

Target Market(s)

People who want to get teir problems resolved, in business, partnership and other personal realms

Industry/Entity Type

Life Coaching

Contact Information for Business Card

Front side should include Name, Phone number, Email, Website and address

Font styles to use
Sans Serif

Colors
add136

Requirements
Must have
• "Mag. Benedikt Haufmoll" -> Name
"Energetische Praxis" -> Jobtitle (describing my profession as life coach)
colours and style should match my website www.dlorvan.net
Nice to have
• a compass as a symbol

```html
<!DOCTYPE html>
<html lang="de">
<head>
<meta charset="utf-8">
<title>Benedikt Haufmoll – Visitenkarte</title>
<link rel="stylesheet" href="https://fonts.googleapis.com/css2?family=Montserrat:ital,wght@0,700;1,400&family=Questrial&display=swap">
<style>
  :root {
    --lime: #add136;
    --navy: #232a40;
    --white: #ffffff;
    --mist: #e6e8ea;
    --backdrop: #dfe5e5;
  }
  * { box-sizing: border-box; margin: 0; padding: 0; }
  html, body { width: 900px; height: 1200px; overflow: hidden; }
  body {
    background: var(--backdrop);
    position: relative;
    font-family: "Questrial", "Century Gothic", sans-serif;
  }
  .card {
    position: absolute;
    left: 162px;
    width: 576px;
    height: 372px;
    overflow: hidden;
  }
  .card--front { top: 153px; background: var(--white); }
  .card--back { top: 650px; background: var(--lime); }

  .front-shapes { position: absolute; inset: 0; }

  .brand-mark {
    position: absolute;
    display: flex;
    align-items: center;
    gap: 8px;
    font-family: "Questrial", "Century Gothic", sans-serif;
  }
  .brand-mark__dot { border-radius: 50%; flex: none; }
  .brand-mark--front { left: 38px; top: 86px; color: var(--navy); font-size: 24px; }
  .brand-mark--front .brand-mark__dot { width: 26px; height: 26px; background: var(--navy); }
  .brand-mark--back {
    left: 0; right: 0; top: 0; bottom: 0;
    justify-content: center;
    color: var(--white); font-size: 54px; gap: 16px;
  }
  .brand-mark--back .brand-mark__dot { width: 54px; height: 54px; background: var(--white); }
  .brand-mark--faint {
    right: -28px; top: 150px;
    color: var(--mist); font-size: 40px;
  }

  .identity {
    position: absolute;
    right: 47px;
    top: 58px;
    text-align: right;
    color: var(--navy);
  }
  .identity__name {
    font-family: "Montserrat", "Century Gothic", sans-serif;
    font-weight: 700;
    font-size: 22.5px;
    letter-spacing: 0.1px;
  }
  .identity__role {
    margin-top: 14px;
    font-family: "Montserrat", "Century Gothic", sans-serif;
    font-style: italic;
    font-weight: 400;
    font-size: 16px;
  }

  .contacts {
    position: absolute;
    left: 46px;
    top: 216px;
    list-style: none;
    color: var(--white);
    font-size: 17px;
  }
  .contacts__item {
    display: flex;
    align-items: center;
    height: 32.7px;
  }
  .contacts__icon {
    width: 20px; height: 20px;
    margin-right: 10px;
    fill: var(--white);
    flex: none;
  }
</style>
</head>
<body>

<section class="card card--front">
  <svg class="front-shapes" viewBox="0 0 576 372" width="576" height="372" aria-hidden="true">
    <polygon points="0,0 576,372 0,372" fill="var(--lime)"/>
    <polygon points="264,170 296,170 276,176" fill="var(--navy)"/>
    <polygon points="266,176 287,176 276,202" fill="var(--white)"/>
  </svg>

  <div class="brand-mark brand-mark--faint" aria-hidden="true">
    <span>Haufmoll</span>
  </div>

  <div class="brand-mark brand-mark--front">
    <span class="brand-mark__dot"></span>
    <span class="brand-mark__name">Haufmoll</span>
  </div>

  <header class="identity">
    <h1 class="identity__name">Mag. Benedikt Haufmoll</h1>
    <p class="identity__role">Energetische Praxis</p>
  </header>

  <ul class="contacts">
    <li class="contacts__item">
      <svg class="contacts__icon" viewBox="0 0 20 20" aria-hidden="true"><path d="M13 1c2 1 3 3 2 5l-1 1-2-3c-1 2-3 7-4 10l3 0-1 2c-2 2-5 2-6 0 2-5 4-10 9-15z"/></svg>
      <span>+43 660 4817392</span>
    </li>
    <li class="contacts__item">
      <svg class="contacts__icon" viewBox="0 0 20 20" aria-hidden="true"><path d="M10 1a9 9 0 1 0 0 18a9 9 0 0 0 0-18zm0 2c1 1 2 3 2 6H8c0-3 1-5 2-6zM3 9c0-3 2-5 4-5-1 1-1 3-1 5H3zm0 2h3c0 2 0 4 1 5-2 0-4-2-4-5zm5 0h4c0 3-1 5-2 6-1-1-2-3-2-6zm6-2c0-2 0-4-1-5 2 0 4 2 4 5h-3z"/></svg>
      <span>www.dlorvan.net</span>
    </li>
    <li class="contacts__item">
      <svg class="contacts__icon" viewBox="0 0 20 20" aria-hidden="true"><path d="M1 4h18v12H1zM2.5 5.5v.4L10 11l7.5-5.1v-.4zM2.5 7.6v6.9h15V7.6L10 12.8z"/></svg>
      <span>benedikt@haufmoll.at</span>
    </li>
    <li class="contacts__item">
      <svg class="contacts__icon" viewBox="0 0 20 20" aria-hidden="true"><path d="M10 0a7 7 0 0 0-7 7c0 5 7 13 7 13s7-8 7-13a7 7 0 0 0-7-7zm0 4a3 3 0 1 1 0 6a3 3 0 0 1 0-6z"/></svg>
      <span>Lindenhofgasse 14, 5020 Salzburg, Österreich</span>
    </li>
  </ul>
</section>

<section class="card card--back">
  <div class="brand-mark brand-mark--back">
    <span class="brand-mark__dot"></span>
    <span class="brand-mark__name">Haufmoll</span>
  </div>
</section>

</body>
</html>
```